Halvoran Books & Consulting Brochure

I need a double sided brochure for a small business bookkeeping & consulting firm.

Halvoran Books & Consulting (I have attached the Logo)

The brochure will be printed on 8.5" x 5.5" paper (Pif).

I'd like to use blues, whites and black colors...

The final product needs to communicate security, professional and current (not futuristic or dated).

I wouldn't mind a picture on 1 of the sides (professional person, a professional meeting, something along those lines).

I am visioning the brochure having 4 sections (2 on front and 2 on back)

Section 1 - Why Outsource Bookkeeping?
Section 2 - Our Philosophy
Section 3 - Services
Section 4 - TBD

I'd like a shell to review before deciding on all of the wording. Some wording is below:

Why Outsource Bookkeeping?

More Time to Focus on your core business
2) Save Money – No More: payroll taxes, workers compensation, benefits, vacation, sick days, office space, hardware, technology, training, turnover…
3) Expertise – you have full time access to a highly skilled team at the cost of a paying a part time bookkeeper.
4) Focused Staff – no more office distractions. Having a remote bookkeeper allows you to focus on your business and allows them to focus on your financials.
5) Access to Top Technology Systems –outsourcing gives you access to the top tool in the industry. You don’t have the time to research and learn about the best financial tools for your business – let an expert handle that
6) Experience – an outsourced bookkeeper can share relevant knowledge gained from experience with other clients

Services:
Bookkeeping Controller Services Accounts Payable Management
Account Receivable Management Check Writing Account Reconciliations
Benchmarking Budgeting Financial Reports
Financial Consulting Profit and Growth Consulting Financial Planning
Succession & Exit Planning Electronic Filing Cabinet Marketing Consulting

Our Philosophy:

Accuracy – having strong financial systems in place that collect and measure all relevant data creates a compliant business and gives you a better understanding of your business.
Understanding – Understanding what financial data is important and what it really means for your business will allow you to take appropriate actions to grow your business or to prevent future issues.
Action – data in meaningless without action, however the right actions put you in control
Control – When you take action based on accurate data that you understand, you are in complete control of your business and its future.

Industry/Entity Type

Small Business

```html
<!DOCTYPE html>
<html lang="en">
<head>
<meta charset="utf-8">
<title>Halvoran Books &amp; Consulting – Brochure Inside</title>
<link rel="stylesheet" href="https://fonts.googleapis.com/css2?family=Questrial&family=Nunito:wght@800&display=swap">
<style>
  :root{
    --sky-pale:#eef8fd;
    --sky-light:#cfe9f7;
    --sky-mid:#8ccaee;
    --sky-deep:#3a8fd3;
    --heading-blue:#1b8fd8;
    --ink:#2e3338;
    --white:#ffffff;
    --photo-office:#46627e;
    --photo-meeting:#c9d6df;
  }
  *{box-sizing:border-box;margin:0;padding:0}
  html,body{width:1200px;height:776px;overflow:hidden;background:var(--white)}
  .brochure{
    position:relative;width:1200px;height:776px;overflow:hidden;
    font-family:"Questrial",sans-serif;color:var(--ink);
  }
  .backdrop{
    position:absolute;inset:0;
    background:
      linear-gradient(125deg,rgba(255,255,255,0) 35%,rgba(255,255,255,.35) 48%,rgba(255,255,255,0) 60%),
      linear-gradient(115deg,var(--sky-pale) 0%,var(--sky-light) 38%,var(--sky-mid) 70%,var(--sky-deep) 100%);
  }
  .section-title{
    position:absolute;background:var(--white);
    font-family:"Nunito",sans-serif;font-weight:800;color:var(--heading-blue);
    font-size:20px;display:flex;align-items:center;
    box-shadow:0 2px 6px rgba(0,60,120,.15);
  }
  .section-title--why{left:0;top:64px;width:384px;height:40px;padding-left:36px}
  .section-title--philosophy{left:980px;top:344px;width:220px;height:44px;padding-left:28px}
  .point-list{position:absolute;list-style:none;font-size:18px;letter-spacing:.3px;line-height:21px;text-align:justify}
  .point-list li{margin-bottom:9px}
  .point-list li::before{content:"◦";color:var(--heading-blue)}
  .point-list .point--ragged{text-align:left}
  .point-list--why{left:18px;top:120px;width:390px}
  .point-list--philosophy{left:798px;top:404px;width:388px}
  .photo{position:absolute;border-radius:50%;border:5px solid rgba(255,255,255,.85);box-shadow:0 0 0 4px rgba(47,134,207,.35)}
  .photo--signing{left:484px;top:82px;width:212px;height:212px;background:radial-gradient(circle at 40% 45%,#e9edf0 0%,#8ea3b6 35%,var(--photo-office) 75%)}
  .photo--meeting{left:465px;top:594px;width:150px;height:150px;background:radial-gradient(circle at 50% 55%,#8a7f78 0%,#b7c4cd 45%,var(--photo-meeting) 80%)}
  .brand{position:absolute;left:966px;top:128px;display:flex;align-items:center;gap:12px}
  .brand-mark{width:84px;height:84px;border-radius:50%;background:var(--white);flex:none}
  .brand-name{font-family:"Questrial",sans-serif;font-size:19px;color:var(--white);line-height:24px;width:130px}
</style>
</head>
<body>
<main class="brochure">
  <div class="backdrop" role="img" aria-label="Decorative background: flowing blue wave lines over a light perspective grid"></div>

  <h2 class="section-title section-title--why">Why Outsource Bookkeeping?</h2>
  <ul class="point-list point-list--why">
    <li>More Time to Focus on your core business</li>
    <li>Save Money – No More: payroll taxes, workers compensation, benefits, vacation, sick days, office space, hardware, technology, training, turnover…</li>
    <li>Expertise – you have full time access to a highly skilled team at the cost of a paying a part time bookkeeper.</li>
    <li>Focused Staff – no more office distractions. Having a remote bookkeeper allows you to focus on your business and allows them to focus on your financials.</li>
    <li>Access to Top Technology Systems – outsourcing gives you access to the top tool in the industry. You don’t have the time to research and learn about the best financial tools for your business – let an expert handle that</li>
    <li class="point--ragged">Experience – an outsourced bookkeeper<br>can share relevant knowledge gained<br>from experience with other clients</li>
  </ul>

  <div class="photo photo--signing" role="img" aria-label="Photo: a professional's hand signing a document with a pen"></div>
  <div class="photo photo--meeting" role="img" aria-label="Photo: two professionals shaking hands across a meeting table"></div>

  <div class="brand">
    <span class="brand-mark"></span>
    <span class="brand-name">Halvoran Books &amp; Consulting</span>
  </div>

  <h2 class="section-title section-title--philosophy">Our Philosophy</h2>
  <ul class="point-list point-list--philosophy">
    <li>Accuracy – having strong financial systems in place that collect and measure all relevant data creates a compliant business and gives you a better understanding of your business.</li>
    <li>Understanding – Understanding what financial data is important and what it really means for your business will allow you to take appropriate actions to grow your business or to prevent future issues.</li>
    <li>Action – data in meaningless without action, however the right actions put you in control</li>
    <li>Control – When you take action based on accurate data that you understand, you are in complete control of your business andits future.</li>
  </ul>
</main>
</body>
</html>
```